Irrigation Business needs their business cards modernised and revamped

I would like to keep my current logo, colours and revamp the format of the card.

I would like the card to be clean yet important.

Im not sure if you include texture but i would like the named logo to be indented into the card etc.

show me something alive and free something thats clinical to the point yet has a feel of achievement. i would like people to go nice card.

Target Market(s)

high end clients, corporate, sports field manger, the guys that make the decisions

Industry/Entity Type

Business

Contact Information for Business Card

nformation to be included

Dorian Hesk (Director)
0487253916
dorian@tfcraft.biz
www.taddsfieldcrafts.com

instagram logo
google logo
facebook logo

Colors

Designer to choose colors to be used in the design.

Requirements
Nice to have
• indentations a really nice feel to the card good texture

```html
<!DOCTYPE html>
<html lang="en">
<head>
<meta charset="utf-8">
<title>Tadd's Field Crafts – Business Card</title>
<link rel="stylesheet" href="https://fonts.googleapis.com/css2?family=Open+Sans:wght@400;600;700;800&display=swap">
<style>
  :root {
    --stage: #2e2e2e;
    --card-white: #f2f2f2;
    --brand-blue: #2b64ad;
    --brand-green: #1e9a4c;
    --text-grey: #3c3c3c;
    --rule: #6f8fb8;
    --back-deep: #2f6db6;
    --back-light: #2ea6da;
    --band: rgba(120, 205, 240, 0.35);
    --social: #e9eef3;
  }
  * { margin: 0; padding: 0; box-sizing: border-box; }
  html, body { width: 1200px; height: 900px; overflow: hidden; }
  body {
    background: var(--stage);
    font-family: "Open Sans", sans-serif;
    position: relative;
  }
  .card {
    position: absolute;
    top: 170px;
    width: 347px;
    height: 561px;
    overflow: hidden;
  }
  /* Front */
  .card--front {
    left: 259px;
    background: var(--card-white);
    text-align: center;
  }
  .brand-mark {
    position: absolute;
    left: 121px;
    top: 76px;
    width: 104px;
    height: 104px;
    border-radius: 50%;
    background: var(--brand-blue);
  }
  .brand-name {
    position: absolute;
    left: 0;
    right: 0;
    top: 188px;
    color: var(--brand-blue);
    font-weight: 800;
    font-size: 29px;
    line-height: 32px;
    letter-spacing: -0.3px;
  }
  .person {
    position: absolute;
    left: 0;
    right: 0;
    top: 371px;
  }
  .person__name {
    color: var(--brand-blue);
    font-weight: 600;
    font-size: 20px;
    line-height: 26px;
  }
  .person__role {
    color: var(--brand-green);
    font-weight: 600;
    font-size: 14px;
    line-height: 20px;
    margin-top: 1px;
  }
  .person__rule {
    width: 132px;
    height: 1px;
    background: var(--rule);
    margin: 9px auto 0;
  }
  .contact-icons {
    display: flex;
    justify-content: center;
    gap: 3px;
    margin-top: 12px;
  }
  .contact-icons svg { width: 19px; height: 19px; display: block; }
  .contact-list {
    list-style: none;
    margin-top: 1px;
    color: var(--text-grey);
    font-size: 14.5px;
    line-height: 21px;
  }
  /* Back */
  .card--back {
    left: 631px;
    background: linear-gradient(135deg, var(--back-deep) 0%, var(--back-light) 45%, var(--back-light) 55%, var(--back-deep) 100%);
  }
  .back-glow {
    position: absolute;
    left: -40px;
    top: 12px;
    width: 427px;
    height: 540px;
    border-radius: 50%;
    background: radial-gradient(ellipse at center, rgba(80, 190, 235, 0.35) 0%, rgba(80, 190, 235, 0) 70%);
  }
  .band {
    position: absolute;
    left: 0;
    right: 0;
    background: var(--band);
  }
  .band--wide { top: 315px; height: 42px; opacity: 0.6; }
  .band--thin-a { top: 360px; height: 6px; }
  .band--thin-b { top: 408px; height: 6px; }
  .band--thin-c { top: 460px; height: 4px; opacity: 0.5; }
  .back-mark {
    position: absolute;
    left: 123px;
    top: 196px;
    width: 100px;
    height: 100px;
    border-radius: 50%;
    background: #ffffff;
  }
  .back-name {
    position: absolute;
    left: 0;
    right: 0;
    top: 308px;
    text-align: center;
    color: #ffffff;
    font-weight: 800;
    font-size: 27px;
    line-height: 31px;
  }
  .social {
    position: absolute;
    left: 0;
    right: 0;
    top: 500px;
    display: flex;
    justify-content: center;
    gap: 7px;
  }
  .social__dot {
    width: 28px;
    height: 28px;
    border-radius: 50%;
    background: var(--social);
  }
</style>
</head>
<body>

  <section class="card card--front">
    <div class="brand-mark"></div>
    <div class="brand-name">TADD'S FIELD<br>CRAFTS</div>

    <div class="person">
      <div class="person__name">DORIAN HESK</div>
      <div class="person__role">DIRECTOR</div>
      <div class="person__rule"></div>

      <div class="contact-icons">
        <svg viewBox="0 0 20 20" aria-label="Phone" role="img">
          <circle cx="10" cy="10" r="10" fill="#2b64ad"/>
          <rect x="5" y="8" width="10" height="6" rx="1.5" fill="#fff"/>
          <rect x="6" y="6" width="8" height="2.5" rx="1" fill="#fff"/>
        </svg>
        <svg viewBox="0 0 20 20" aria-label="Email" role="img">
          <circle cx="10" cy="10" r="10" fill="#2b64ad"/>
          <rect x="5" y="6.5" width="10" height="7" rx="0.8" fill="#fff"/>
          <path d="M5 7l5 4 5-4" fill="none" stroke="#2b64ad" stroke-width="1"/>
        </svg>
        <svg viewBox="0 0 20 20" aria-label="Website" role="img">
          <circle cx="10" cy="10" r="10" fill="#2b64ad"/>
          <circle cx="10" cy="10" r="5" fill="none" stroke="#fff" stroke-width="1.4"/>
          <path d="M5 10h10M10 5v10" stroke="#fff" stroke-width="1"/>
        </svg>
      </div>

      <ul class="contact-list">
        <li>0487253916</li>
        <li>dorian@tfcraft.biz</li>
        <li>www.taddsfieldcrafts.com</li>
      </ul>
    </div>
  </section>

  <section class="card card--back">
    <div class="back-glow"></div>
    <div class="band band--wide"></div>
    <div class="band band--thin-a"></div>
    <div class="band band--thin-b"></div>
    <div class="band band--thin-c"></div>

    <div class="back-mark"></div>
    <div class="back-name">TADD'S FIELD<br>CRAFTS</div>

    <div class="social" aria-label="Social profiles">
      <span class="social__dot"></span>
      <span class="social__dot"></span>
      <span class="social__dot"></span>
    </div>
  </section>

</body>
</html>
```